QRV Stationery Design Project

Dear Designers,
We need a new stationery design for company to match our new logo.
Designers should provide a design for the following:
1. Business Card: 3.5x2 Inches.
2. Letterhead: A4 size.
3. Envelops: 25x35.5 Cm.
You can keep the Arabic name at the bottom of the logo Or you can use the separate attached Arabic Name.
Please refer to the attached logo guide for design information.
Sample Business Card information:
Name: Tariq Nawaf
Position: Operation Manager
Tel: +966 920007714 Ex. 500
Fax: +966 (3)8842617
Mob: +966 (5)00387251
email: tariq@qrv-example.com.sa
URL: www.qrv-example.com.sa
Address:
Al Wadi Tower, Suite 303
Nasser bin Salem Str.
Khobar, 31847
Saudi Arabia
Updates
Dear All,
Please note, we had uploaded our logo along with Arabic writing in Adobe illustrator format (.ai).
Regards,
Khalid
Dear All,
A sample data for the business card had been added as per your request.
Regards,
Khalid

```html
<!DOCTYPE html>
<html lang="en">
<head>
<meta charset="utf-8">
<title>QRV Letterhead</title>
<link rel="stylesheet" href="https://fonts.googleapis.com/css2?family=Saira:wght@400;700&display=swap">
<style>
  :root {
    --navy: #0f2d52;
    --paper: #ffffff;
    --edge: #a6a6a6;
    --footer-text: #ffffff;
  }
  html, body {
    margin: 0;
    padding: 0;
    width: 848px;
    height: 1200px;
    overflow: hidden;
    background: var(--paper);
  }
  .letterhead {
    position: relative;
    width: 848px;
    height: 1200px;
    box-sizing: border-box;
    border: 1px solid var(--edge);
    background: var(--paper);
    font-family: "Saira", "Arial", sans-serif;
  }
  .brand {
    position: absolute;
    top: 34px;
    right: 26px;
    width: 270px;
    height: 76px;
    display: flex;
    align-items: center;
    justify-content: flex-end;
    gap: 14px;
  }
  .brand-mark {
    width: 22px;
    height: 22px;
    background: var(--navy);
  }
  .brand-name {
    margin: 0;
    font-size: 52px;
    font-weight: 700;
    line-height: 1;
    letter-spacing: 2px;
    color: var(--navy);
  }
  .contact-band {
    position: absolute;
    left: 21px;
    right: 20px;
    top: 1134px;
    height: 52px;
    background: var(--navy);
    color: var(--footer-text);
    display: flex;
    flex-direction: column;
    justify-content: center;
    align-items: center;
    font-size: 14px;
    font-weight: 400;
    line-height: 18px;
    text-align: center;
    white-space: nowrap;
  }
  .contact-band p { margin: 0; }
</style>
</head>
<body>
  <div class="letterhead">
    <header class="brand">
      <span class="brand-mark"></span>
      <h1 class="brand-name">QRV</h1>
    </header>

    <footer class="contact-band">
      <p class="address-line">Al Wadi Tower, Suite 303, Nasser bin Salem Str., Khobar, 31847, Saudi Arabia</p>
      <p class="contact-line">Tel: +966 920007714 Ex. 500 | Fax: +966 (3)8842617 | email: tariq@qrv-example.com.sa | URL: www.qrv-example.com.sa</p>
    </footer>
  </div>
</body>
</html>
```